Business Card Design for a Sound engineer and DJ

We would like a residn of the business card.

Logo must remain the same.
The card is for the owner of the company.
The business card is in Arabic as the company is based in Kuwait.
The company specializes in sound engineering for singers concerts and events and in addition DJ.
The color options is up to the designer but we would like it masculine as the owner is a man.

Target Market(s)

All ages

Industry/Entity Type

Media

Contact Information for Business Card

Name:
Eng. Faisal Barrak
م/فيصل براك

The name above is in Arabic and English.

Title: General Manager
Mobile: +965 96370482
Office: +965 22480637
Email: info@qamarwave.net

Address:
Office no. 3
1st floor
Marjan Complex
Hamad Faraj St.
Salmiya
Kuwait

Instagram: @qamarwave
Snap: qamarwave

Requirements
Nice to have
• can we have Instagram icon and snap icon and a phone vector and email?
• Instead of writing the words

```html
<!DOCTYPE html>
<html lang="en">
<head>
<meta charset="utf-8">
<title>Qamar Wave – Business Card</title>
<link rel="stylesheet" href="https://fonts.googleapis.com/css2?family=Tinos:wght@400;700&family=Noto+Naskh+Arabic:wght@400;700&display=swap">
<style>
  :root{
    --stage:#e8e5e0;
    --card:#fbfbfa;
    --brand:#7b52b3;
    --name:#5a6cc0;
    --ink:#161616;
    --rule:#6aa6dc;
    --divider:#222;
    --icon:#6f7fcf;
  }
  *{box-sizing:border-box;margin:0;padding:0}
  html,body{width:1200px;height:892px;overflow:hidden;background:var(--stage)}
  .stage{position:relative;width:1200px;height:892px;display:flex;flex-direction:column;align-items:center;justify-content:center;gap:40px}
  .card{position:relative;width:640px;height:366px;background:var(--card);box-shadow:0 6px 18px rgba(0,0,0,.18)}

  /* front */
  .card--front{display:flex;flex-direction:column;align-items:center;justify-content:center;gap:14px}
  .brand{display:flex;align-items:center;gap:14px}
  .brand__mark{width:18px;height:18px;background:var(--brand)}
  .brand__name{font-family:"Tinos",serif;font-weight:700;font-size:54px;letter-spacing:6px;color:var(--brand)}
  .tagline{font-family:"Tinos",serif;font-size:19px;letter-spacing:3px;color:var(--brand)}
  .tagline-ar{font-family:"Noto Naskh Arabic",serif;font-size:20px;color:var(--brand)}

  /* back */
  .card--back .brand-block{position:absolute;left:40px;top:40px;width:330px;display:flex;flex-direction:column;align-items:center;gap:8px}
  .card--back .brand__name{font-size:36px;letter-spacing:4px}
  .card--back .brand__mark{width:13px;height:13px}
  .card--back .tagline{font-size:13px;letter-spacing:2px}
  .card--back .tagline-ar{font-size:14px}
  .divider{position:absolute;left:392px;top:60px;width:1px;height:190px;background:var(--divider)}
  .snap{position:absolute;left:40px;top:250px;width:330px;display:flex;align-items:center;justify-content:center;gap:10px;font-family:"Tinos",serif;font-weight:700;font-size:15px;color:var(--ink)}
  .snap__box{width:24px;height:24px;background:#1b1b1b;border-radius:3px}
  .rule{position:absolute;left:28px;right:28px;top:292px;height:1px;background:var(--rule)}
  .address{position:absolute;left:0;right:0;top:304px;text-align:center;font-family:"Tinos",serif;font-weight:700;font-size:15px;color:var(--ink)}
  .person{position:absolute;left:418px;top:78px;right:24px}
  .person__name{font-family:"Tinos",serif;font-weight:700;font-size:27px;color:var(--name)}
  .person__name-ar{font-family:"Noto Naskh Arabic",serif;font-size:19px;color:var(--name);line-height:1.3}
  .person__title{font-family:"Tinos",serif;font-size:16px;color:var(--ink)}
  .contacts{position:absolute;left:418px;top:180px;list-style:none;display:flex;flex-direction:column;gap:5px}
  .contacts li{display:flex;align-items:center;gap:10px;font-family:"Tinos",serif;font-weight:700;font-size:15px;color:var(--ink)}
  .contacts svg{width:13px;height:13px;flex:none}
</style>
</head>
<body>
<main class="stage">
  <section class="card card--back" aria-label="Business card back">
    <div class="brand-block">
      <div class="brand"><span class="brand__mark"></span><span class="brand__name">Qamar Wave</span></div>
      <p class="tagline">DJ - SOUND ENG. - LIGHTING</p>
      <p class="tagline-ar" dir="rtl">دي جي - هندسة صوت - إضاءة</p>
    </div>
    <div class="divider"></div>
    <div class="person">
      <p class="person__name">Faisal Barrak</p>
      <p class="person__name-ar" dir="rtl" lang="ar">م/فيصل براك</p>
      <p class="person__title">General Manager</p>
    </div>
    <ul class="contacts">
      <li><svg viewBox="0 0 13 13"><rect width="13" height="13" rx="2" fill="var(--icon)"/><path d="M4 3.5c0 3 2.5 5.5 5.5 5.5l.5-1.5-1.6-.7-.7.8c-1-.5-1.8-1.3-2.3-2.3l.8-.7L5.5 3z" fill="#fff"/></svg>+965 22480637</li>
      <li><svg viewBox="0 0 13 13"><rect width="13" height="13" rx="2" fill="var(--icon)"/><rect x="4.3" y="2.5" width="4.4" height="8" rx=".8" fill="#fff"/></svg>+965 96370482</li>
      <li><svg viewBox="0 0 13 13"><rect width="13" height="13" rx="2" fill="var(--icon)"/><rect x="2.5" y="3.8" width="8" height="5.4" fill="#fff"/><path d="M2.5 3.8l4 3 4-3" fill="none" stroke="var(--icon)" stroke-width=".9"/></svg>info@qamarwave.net</li>
      <li><svg viewBox="0 0 13 13"><rect width="13" height="13" rx="2" fill="var(--icon)"/></svg>@qamarwave</li>
    </ul>
    <div class="snap"><span class="snap__box"></span><span>Snap: qamarwave</span></div>
    <div class="rule"></div>
    <p class="address">Office no. 3 1st floor Marjan Complex Hamad Faraj St. Salmiya, Kuwait</p>
  </section>

  <section class="card card--front" aria-label="Business card front">
    <div class="brand"><span class="brand__mark"></span><span class="brand__name">Qamar Wave</span></div>
    <p class="tagline">DJ - SOUND ENG. - LIGHTING</p>
    <p class="tagline-ar" dir="rtl">دي جي - هندسة صوت - إضاءة</p>
  </section>
</main>
</body>
</html>
```